Advertising Portal Needs eBrochure

Hi Crowders! Our advertising portal, which focus on the new launches property, needs an online brochure to promote to potential advertisers the benefits of advertising their projects with us. These advertisers will be mainly real estate developers and agencies.

WHAT WE LOOKING FOR
We do not want over-fanciful designs that makes the content hard to read. The use of illustrations and graphics/symbols related to covered topics are encouraged. The overall design should portrait our advertising efficiency through online and social media means. Our website - www.brightkeyhomes.sg.

For draft purposes, just do up the front page, back page, and few inner pages, preferably to include one illustration chart (either on page 7/8). Size wise probably A5 portrait or landscape, for future printing into a booklet.

WORK COMPLETION AND PAYMENT
The $500 stated here is 50% of the payment. Upon getting a desired draft design, we will need you to work on the full content with slight amendments along the way. Once done, we will be paying the balance $500, and we will need the pdf file as well as the work file.

Let your design juice flow, and hope we can work with you!
Updates

Hi Crowders! Thank you for your submissions. We are closing the project as we've decided on a design. It's a pity we can only select one design, as there are a number of good works. Hope we will have a chance to work together on our upcoming projects. Cheers =)

Target Market(s)

Real estate developers, real estate agencies, and perhaps to an extent, individual property sales agent.

Industry/Entity Type

Advertising

Requirements
Should not have
• We prefer not to have much real people kind of stock images. Try not to use images from our portal as we do not have the ownerships. Instead, you can use stock images of property developments artist impression that gives a similar feel.

```html
<!DOCTYPE html>
<html lang="en">
<head>
<meta charset="utf-8">
<title>Bright Key Homes – Advertiser eBrochure Spread</title>
<link href="https://fonts.googleapis.com/css2?family=Montserrat:wght@400;600;700;800&family=Open+Sans:wght@400;600&display=swap" rel="stylesheet">
<style>
  :root{
    --backdrop:#e6e6e3;
    --slate-dark:#2b2f35;
    --slate-mid:#434a52;
    --slate-faint:rgba(255,255,255,0.06);
    --lime:#8cc63f;
    --lime-dark:#5a9e2a;
    --green-page:#6fb83a;
    --green-deep:#3f8b24;
    --sky:#3fa9e0;
    --sky-dark:#1f6fa8;
    --mint:#a7d8c9;
    --navy:#17446b;
    --sun:#f2e64a;
    --paper:#ffffff;
    --ink-soft:#d7dde2;
  }
  *{box-sizing:border-box;margin:0;padding:0}
  html,body{width:1200px;height:900px;overflow:hidden;background:var(--backdrop)}
  body{font-family:"Open Sans",Arial,sans-serif;position:relative}
  .spread{position:absolute;left:50px;top:110px;width:1100px;height:680px;display:flex;box-shadow:0 8px 30px rgba(0,0,0,.25)}
  .page{position:relative;width:550px;height:680px;overflow:hidden}

  /* left page */
  .page--active{background:linear-gradient(135deg,var(--slate-mid),var(--slate-dark))}
  .backdrop-words{position:absolute;inset:0;font-family:"Montserrat",sans-serif;font-weight:800;color:var(--slate-faint);line-height:.95;text-transform:uppercase}
  .backdrop-words span{position:absolute;white-space:nowrap}
  .campaign-title{position:absolute;left:210px;top:70px;width:300px;font-family:"Montserrat",sans-serif;font-weight:600;font-size:13px;color:var(--paper);line-height:1.3}
  .channel-heading{position:absolute;left:24px;top:140px;font-family:"Montserrat",sans-serif;font-weight:700;font-size:17px;color:var(--paper);letter-spacing:.5px}
  .channel-copy{position:absolute;left:24px;top:168px;width:150px;font-size:9.5px;line-height:1.55;color:var(--ink-soft)}
  .accent-rule{position:absolute;left:186px;top:120px;width:4px;height:420px;background:var(--lime)}
  .channel-box{position:absolute;left:200px;width:92px;height:32px;display:flex;align-items:center;justify-content:center;font-family:"Montserrat",sans-serif;font-weight:600;font-size:12px;color:var(--paper)}
  .channel-box--search{top:196px;background:var(--lime)}
  .channel-box--social{top:252px;background:var(--sky)}
  .channel-box--print{top:308px;background:var(--mint);color:var(--slate-dark)}
  .channel-note{position:absolute;left:302px;width:98px;font-size:8.5px;line-height:1.4;color:var(--ink-soft)}
  .flow-arrows{position:absolute;left:404px;top:196px}
  .project-tag{position:absolute;left:458px;top:250px;font-family:"Montserrat",sans-serif;font-weight:700;font-size:16px;color:var(--paper);line-height:1.15}
  .caption{position:absolute;font-size:10px;font-style:italic;color:var(--paper)}
  .page--active .caption{left:260px;top:600px}

  /* right page */
  .page--passive{background:linear-gradient(160deg,var(--green-page),var(--green-deep))}
  .section-heading{position:absolute;left:24px;top:40px;display:flex;align-items:center;gap:8px;font-family:"Montserrat",sans-serif;font-weight:700;font-size:12.5px;color:var(--paper);text-transform:uppercase}
  .section-number{width:24px;height:24px;border-radius:50%;background:var(--paper);color:var(--green-deep);display:flex;align-items:center;justify-content:center;font-size:14px}
  .intro-copy{position:absolute;left:24px;top:120px;width:165px;font-size:9.5px;line-height:1.55;color:var(--paper)}
  .sub-heading{position:absolute;left:24px;top:210px;font-family:"Montserrat",sans-serif;font-weight:700;font-size:11px;color:var(--paper)}
  .detail-copy{position:absolute;left:24px;top:230px;width:165px;font-size:9.5px;line-height:1.55;color:var(--paper)}
  .footnote-copy{position:absolute;left:24px;top:310px;width:165px;font-size:9px;color:var(--navy)}
  .reach-chart{position:absolute;left:190px;top:120px}
  .page--passive .caption{left:260px;top:490px}
  .gutter{position:absolute;left:540px;top:0;width:20px;height:680px;background:linear-gradient(90deg,transparent,rgba(0,0,0,.25),transparent);pointer-events:none}
</style>
</head>
<body>
<div class="spread">
  <section class="page page--active">
    <div class="backdrop-words" aria-hidden="true">
      <span style="left:-10px;top:40px;font-size:70px">Online</span>
      <span style="left:-20px;top:150px;font-size:90px">Search</span>
      <span style="left:-30px;top:290px;font-size:78px">Media</span>
      <span style="left:-10px;top:420px;font-size:64px">Advertise</span>
      <span style="left:-20px;top:530px;font-size:92px">Company</span>
    </div>
    <p class="campaign-title">Online and Marketing Campaigns Boost your Project Exposure</p>
    <h2 class="channel-heading">EMAIL BLASTING</h2>
    <p class="channel-copy">Reach thousands of property buyers directly in their inbox with weekly launch updates. Each blast features your project with images, key facts and a clear call to action. Campaigns are tracked so you see opens and clicks.</p>
    <div class="accent-rule"></div>
    <div class="channel-box channel-box--search">Searchly</div>
    <div class="channel-box channel-box--social">Friendloop</div>
    <div class="channel-box channel-box--print">Daily Courier</div>
    <p class="channel-note" style="top:198px">Search ads place your launch on top results</p>
    <p class="channel-note" style="top:254px">Social posts reach active home seekers daily</p>
    <p class="channel-note" style="top:310px">Featured listings in print weekly</p>
    <svg class="flow-arrows" width="50" height="144" viewBox="0 0 50 144" aria-hidden="true">
      <polygon points="0,0 18,0 48,66 38,72 0,32" fill="#8cc63f"/>
      <polygon points="0,56 36,56 48,72 36,88 0,88" fill="#3fa9e0"/>
      <polygon points="0,112 38,72 48,78 18,144 0,144" fill="#a7d8c9"/>
    </svg>
    <p class="project-tag">YOUR<br>PROJECT</p>
    <p class="caption">Illustration 1: Active Marketing</p>
  </section>

  <section class="page page--passive">
    <h2 class="section-heading"><span class="section-number">3</span>Your project gains high awareness from brightkeyhomes.sg</h2>
    <p class="intro-copy">Every visit to our portal places your project in front of buyers who are already searching for new homes.</p>
    <h3 class="sub-heading">STEADY TRAFFIC</h3>
    <p class="detail-copy">Daily traffic keeps your listing visible long after launch day, building trust and steady enquiries.</p>
    <p class="footnote-copy">Your project is seen all year round.</p>
    <svg class="reach-chart" width="350" height="350" viewBox="0 0 350 350" font-family="Montserrat, sans-serif">
      <circle cx="135" cy="175" r="130" fill="#3fa9e0" stroke="#1f6fa8" stroke-width="6"/>
      <circle cx="135" cy="175" r="102" fill="#f2e64a"/>
      <circle cx="135" cy="175" r="90" fill="#1f6fa8"/>
      <circle cx="135" cy="175" r="64" fill="#5a9e2a" stroke="#8cc63f" stroke-width="4"/>
      <circle cx="135" cy="175" r="32" fill="#17446b"/>
      <text x="135" y="179" text-anchor="middle" font-size="10" font-weight="700" fill="#fff">Project</text>
      <text x="135" y="64" text-anchor="middle" font-size="10" font-weight="600" fill="#fff">Portal Visitors</text>
      <text x="135" y="134" text-anchor="middle" font-size="8.5" fill="#fff">Search</text>
      <text x="135" y="222" text-anchor="middle" font-size="8.5" fill="#fff">Listings</text>
      <text x="85" y="178" text-anchor="middle" font-size="8.5" fill="#fff">Social</text>
      <text x="185" y="178" text-anchor="middle" font-size="8.5" fill="#fff">Email</text>
      <path d="M205 190 Q240 215 266 200" fill="none" stroke="#fff" stroke-width="2"/>
      <polygon points="266,194 276,200 266,206" fill="#fff"/>
      <text x="276" y="166" font-size="13" font-weight="700" fill="#fff">YOUR</text>
      <text x="276" y="182" font-size="13" font-weight="700" fill="#fff">PROJECT</text>
    </svg>
    <p class="caption">Illustration 2: Passive Marketing</p>
  </section>
  <div class="gutter"></div>
</div>
</body>
</html>
```